Design business cards for Valturon

I am looking for a clean, crisp and professional business card design. A logo already exists with which to work, which is attached in various formats. The design needs to be print ready. A clear brief is attached - please read it carefully and ensure you can deliver what is required. Looking forward to awarding the prize to a great design and great designer!

```html
<!DOCTYPE html>
<html lang="en">
<head>
<meta charset="utf-8">
<title>Valturon business cards</title>
<link rel="stylesheet" href="https://fonts.googleapis.com/css2?family=Alegreya:wght@400;700&display=swap">
<style>
  :root {
    --bg: #e4e5e8;
    --card: #ffffff;
    --ink: #2b2b2b;
    --ink-soft: #444444;
    --red: #d9432b;
    --orange: #f08a24;
    --amber: #f6b041;
  }
  * { box-sizing: border-box; margin: 0; padding: 0; }
  html, body { width: 1200px; height: 720px; overflow: hidden; }
  body {
    background: var(--bg);
    font-family: "Alegreya", Georgia, serif;
    color: var(--ink);
    position: relative;
  }
  .card {
    position: absolute;
    top: 195px;
    width: 540px;
    height: 330px;
    background: var(--card);
    overflow: hidden;
    box-shadow: 0 6px 18px rgba(0,0,0,0.12);
  }
  .card--front { left: 40px; }
  .card--back { left: 620px; }

  .corner-tab { position: absolute; }
  .corner-tab--top-right { top: -10px; right: -10px; width: 80px; height: 80px; }
  .corner-tab--left { top: 200px; left: -22px; width: 48px; height: 60px; }
  .corner-tab--bottom-left { bottom: -14px; left: -16px; width: 60px; height: 84px; }

  .tagline {
    position: absolute; top: 26px; left: 30px;
    font-size: 19px; color: var(--ink-soft);
  }
  .brand {
    position: absolute; top: 105px; left: 60px;
    display: flex; align-items: center; gap: 24px;
  }
  .brand__dot {
    width: 62px; height: 62px; border-radius: 50%;
    background: var(--orange);
  }
  .brand__name { font-size: 68px; font-weight: 400; color: var(--ink); letter-spacing: 1px; }
  .address {
    position: absolute; top: 262px; left: 150px;
    font-size: 13px; color: var(--ink-soft);
  }

  .mini-brand {
    position: absolute; top: 24px; right: 30px;
    display: flex; align-items: center; gap: 8px;
  }
  .mini-brand__dot { width: 16px; height: 16px; border-radius: 50%; background: var(--orange); }
  .mini-brand__name { font-size: 18px; color: var(--ink); }

  .person { position: absolute; top: 70px; left: 72px; }
  .person__name { font-size: 24px; font-weight: 700; color: var(--ink); line-height: 1.2; }
  .person__name .first { color: var(--red); }
  .person__creds, .person__role { font-size: 13px; color: var(--ink-soft); margin-top: 3px; }

  .contacts {
    position: absolute; top: 160px; left: 72px;
    display: grid; grid-template-columns: 68px auto; row-gap: 2px;
    font-size: 14px; line-height: 20px; color: var(--ink-soft);
  }
  .band { position: absolute; right: 0; bottom: 0; width: 340px; height: 56px; }
  .band__url {
    position: absolute; right: 26px; bottom: 17px;
    font-size: 16px; color: #ffffff; letter-spacing: 0.5px;
  }
</style>
</head>
<body>

<section class="card card--front">
  <svg class="corner-tab corner-tab--top-right" viewBox="0 0 80 80" role="img" aria-label="Warm orange corner accent">
    <defs>
      <linearGradient id="tabWarm" x1="0" y1="0" x2="1" y2="1">
        <stop offset="0" stop-color="#f6b041"/><stop offset="1" stop-color="#e2572b"/>
      </linearGradient>
    </defs>
    <rect x="0" y="0" width="80" height="80" rx="12" fill="url(#tabWarm)"/>
  </svg>
  <svg class="corner-tab corner-tab--left" viewBox="0 0 48 60" role="img" aria-label="Warm orange edge accent">
    <rect x="0" y="0" width="48" height="60" rx="10" fill="url(#tabWarm)"/>
  </svg>

  <p class="tagline">design is the expression of intent</p>
  <div class="brand">
    <span class="brand__dot"></span>
    <span class="brand__name">Valturon</span>
  </div>
  <p class="address">42 Wattle Grove, Kew East Victoria 3102 Australia</p>
</section>

<section class="card card--back">
  <div class="mini-brand">
    <span class="mini-brand__dot"></span>
    <span class="mini-brand__name">Valturon</span>
  </div>

  <div class="person">
    <h1 class="person__name"><span class="first">Daniel</span> Harcourt</h1>
    <p class="person__creds">BE(Hons) PhD MIEAust GAICD</p>
    <p class="person__role">Director, Principal Consultant</p>
  </div>

  <div class="contacts">
    <span>phone</span><span>+61 (0)400 555 017</span>
    <span>e-mail</span><span>dharcourt@valturon.com.au</span>
    <span>chat</span><span>dan.harcourt22</span>
    <span>profile</span><span>www.valturon.com.au/team/dharcourt</span>
  </div>

  <svg class="corner-tab corner-tab--bottom-left" viewBox="0 0 60 84" role="img" aria-label="Warm orange corner accent">
    <defs>
      <linearGradient id="tabWarmBack" x1="0" y1="0" x2="1" y2="1">
        <stop offset="0" stop-color="#f6b041"/><stop offset="1" stop-color="#e2572b"/>
      </linearGradient>
    </defs>
    <rect x="0" y="0" width="60" height="84" rx="12" fill="url(#tabWarmBack)"/>
  </svg>

  <svg class="band" viewBox="0 0 340 56" preserveAspectRatio="none">
    <polygon points="50,0 340,0 340,56 0,56" fill="#d9432b"/>
    <polygon points="0,56 30,26 90,56" fill="#f08a24" opacity="0.8"/>
  </svg>
  <p class="band__url">www.valturon.com.au</p>
</section>

</body>
</html>
```